Landscaping company needs bold flyer

We are a new landscaping company that requires a flyer to advertise our business. It should be bold and reflect our creative outlook. Our services include paving, driveways, fencing, brickwork, planting and turfing and artificial grass. We pride ourself on quality workmanship at an affordable price. Here is the link to our website http://www.brackmoor-yards.com/

Industry/Entity Type

Landscaping

Font styles to use
Sans Serif

Colors
000000
9bcb3c

Requirements
Nice to have
• I'd like a design without any photographs on it. My brother has had some leaflets designed which I like,I'd like something similar. I've uploaded pictures of them.
Should not have
• The designs that have been submitted thus far have all been very simlilar. Could someone please try to create an original design, maybe with out any pictures on it. Please do not copy directly from my website, the link is purely for information

```html
<!DOCTYPE html>
<html lang="en">
<head>
<meta charset="utf-8">
<title>Brackmoor Yards – Landscaping Flyer</title>
<link rel="stylesheet" href="https://fonts.googleapis.com/css2?family=Source+Sans+3:wght@400;600;700&family=Montserrat:wght@800&display=swap">
<style>
  :root {
    --black: #000000;
    --lime: #9bcb3c;
    --lime-bright: #8dc63f;
    --forest: #2f7d3a;
    --white: #ffffff;
    --paper: #f2f2f2;
    --ink: #1a1a1a;
  }
  * { margin: 0; padding: 0; box-sizing: border-box; }
  html, body { width: 950px; height: 1200px; overflow: hidden; background: var(--white); }
  .flyer {
    position: relative;
    width: 950px;
    height: 1200px;
    font-family: "Source Sans 3", Arial, sans-serif;
    overflow: hidden;
  }
  .flyer__shapes { position: absolute; inset: 0; }
  .brand {
    position: absolute;
    top: 42px; left: 0; width: 100%;
    display: flex; justify-content: center; align-items: center; gap: 14px;
  }
  .brand__dot { width: 26px; height: 26px; border-radius: 50%; background: var(--lime-bright); }
  .brand__name {
    font-family: "Montserrat", Arial, sans-serif;
    font-weight: 800;
    font-size: 50px;
    letter-spacing: -1px;
    color: var(--black);
    line-height: 1;
  }
  .pitch {
    position: absolute; top: 632px; left: 0; width: 100%;
    text-align: center;
  }
  .pitch__headline {
    color: var(--white);
    font-weight: 400;
    font-size: 31px;
    line-height: 40px;
    text-transform: uppercase;
  }
  .pitch__sub {
    margin-top: 18px;
    color: var(--lime-bright);
    font-weight: 600;
    font-size: 22px;
  }
  .services {
    position: absolute; top: 789px; left: 0; width: 100%;
  }
  .service {
    position: absolute;
    width: 200px;
    margin-left: -100px;
    text-align: center;
  }
  .service__icon { display: block; width: 98px; height: 98px; margin: 0 auto; }
  .service__icon .tile { fill: none; stroke: var(--lime); stroke-width: 3; }
  .service__icon .glyph { fill: none; stroke: var(--lime); stroke-width: 3.5; stroke-linecap: round; stroke-linejoin: round; }
  .service__label {
    margin-top: 10px;
    color: var(--white);
    font-size: 14px;
    font-weight: 400;
    text-transform: uppercase;
    letter-spacing: -0.2px;
  }
  .contact {
    position: absolute; top: 1114px; left: 0; width: 100%;
    display: flex; justify-content: center; align-items: center; gap: 16px;
    padding-left: 24px;
  }
  .contact__cta { font-size: 23px; font-weight: 400; color: var(--ink); }
  .contact__phone {
    display: flex; align-items: center; gap: 8px;
    font-size: 33px; font-weight: 700; color: var(--ink);
  }
  .contact__web {
    position: absolute; top: 1152px; left: 0; width: 100%;
    text-align: center; padding-left: 24px;
    font-size: 29px; font-weight: 600; color: var(--lime-bright);
    text-transform: uppercase;
  }
  .social {
    position: absolute; top: 1156px; left: 32px;
    display: flex; gap: 18px;
  }
  .social__square { width: 28px; height: 28px; border-radius: 4px; background: var(--lime-bright); }
</style>
</head>
<body>
<main class="flyer">
  <svg class="flyer__shapes" width="950" height="1200" viewBox="0 0 950 1200">
    <defs>
      <linearGradient id="garden-tones" x1="0" y1="0" x2="1" y2="1">
        <stop offset="0" stop-color="#3f6b26"/>
        <stop offset="0.45" stop-color="#6f8f3a"/>
        <stop offset="0.7" stop-color="#c9b88a"/>
        <stop offset="1" stop-color="#8fae2e"/>
      </linearGradient>
      <linearGradient id="band-green" x1="0" y1="0" x2="1" y2="0">
        <stop offset="0" stop-color="var(--forest)"/>
        <stop offset="1" stop-color="var(--lime-bright)"/>
      </linearGradient>
      <linearGradient id="band-green-rev" x1="0" y1="0" x2="1" y2="0">
        <stop offset="0" stop-color="var(--lime-bright)"/>
        <stop offset="1" stop-color="var(--forest)"/>
      </linearGradient>
      <linearGradient id="patio-tones" x1="0" y1="0" x2="1" y2="1">
        <stop offset="0" stop-color="#8a7a62"/>
        <stop offset="0.35" stop-color="#a9adb0"/>
        <stop offset="1" stop-color="#c6c9cb"/>
      </linearGradient>
    </defs>

    <rect class="garden-photo" x="0" y="100" width="950" height="540" fill="url(#garden-tones)" role="img" aria-label="Photo of a landscaped garden with a winding gravel path between shrubs and trees"/>

    <path class="header-band" d="M0,125 Q475,225 950,115 L950,142 Q475,258 0,152 Z" fill="url(#band-green)"/>
    <path class="header-bg" d="M0,0 H950 V115 Q475,225 0,125 Z" fill="var(--white)"/>

    <path class="body-band" d="M0,602 Q475,478 950,612 L950,630 Q475,505 0,625 Z" fill="url(#band-green)"/>
    <path class="body-bg" d="M0,625 Q475,505 950,630 V1200 H0 Z" fill="var(--black)"/>

    <circle class="patio-photo" cx="831" cy="521" r="90" fill="url(#patio-tones)" stroke="var(--lime-bright)" stroke-width="7" role="img" aria-label="Photo of a finished stone patio beside a wooden fence"/>

    <path class="footer-band" d="M0,1128 Q475,1018 950,1120 L950,1136 Q475,1041 0,1141 Z" fill="url(#band-green-rev)"/>
    <path class="footer-bg" d="M0,1141 Q475,1041 950,1136 V1200 H0 Z" fill="var(--paper)"/>
  </svg>

  <header class="brand">
    <span class="brand__dot"></span>
    <span class="brand__name">BRACKMOOR YARDS</span>
  </header>

  <section class="pitch">
    <h1 class="pitch__headline">We pride ourself on quality workmanship<br>at an affordable price</h1>
    <p class="pitch__sub">Brackmoor Yards are fully insured, offering peace of mind.</p>
  </section>

  <section class="services">
    <div class="service" style="left:213px;top:0">
      <svg class="service__icon" viewBox="0 0 100 100" aria-hidden="true">
        <rect class="tile" x="4" y="4" width="92" height="92" rx="18"/>
        <g class="glyph">
          <path d="M38,26 L26,74"/>
          <path d="M62,26 L74,74"/>
          <path d="M50,30 V38 M50,46 V54 M50,62 V70"/>
        </g>
      </svg>
      <p class="service__label">Driveways</p>
    </div>
    <div class="service" style="left:478px;top:0">
      <svg class="service__icon" viewBox="0 0 100 100" aria-hidden="true">
        <rect class="tile" x="4" y="4" width="92" height="92" rx="18"/>
        <g class="glyph">
          <path d="M28,72 L30,62 L62,30 L70,38 L38,70 Z"/>
          <path d="M56,36 L64,44"/>
          <path d="M26,30 H46"/>
          <path d="M54,72 H74"/>
        </g>
      </svg>
      <p class="service__label">Garden Design</p>
    </div>
    <div class="service" style="left:708px;top:0">
      <svg class="service__icon" viewBox="0 0 100 100" aria-hidden="true">
        <rect class="tile" x="4" y="4" width="92" height="92" rx="18"/>
        <g class="glyph">
          <rect x="24" y="28" width="52" height="44"/>
          <path d="M24,42.7 H76 M24,57.3 H76"/>
          <path d="M50,28 V42.7 M37,42.7 V57.3 M63,42.7 V57.3 M50,57.3 V72"/>
        </g>
      </svg>
      <p class="service__label">Paving &amp; Brickwork</p>
    </div>
    <div class="service" style="left:213px;top:140px">
      <svg class="service__icon" viewBox="0 0 100 100" aria-hidden="true">
        <rect class="tile" x="4" y="4" width="92" height="92" rx="18"/>
        <g class="glyph">
          <path d="M24,72 H76"/>
          <path d="M50,72 V44"/>
          <path d="M50,52 C42,52 34,46 34,36 C44,36 50,42 50,52"/>
          <path d="M50,46 C50,36 58,28 68,28 C68,38 60,46 50,46"/>
        </g>
      </svg>
      <p class="service__label">Planting &amp; Turfing</p>
    </div>
    <div class="service" style="left:478px;top:140px">
      <svg class="service__icon" viewBox="0 0 100 100" aria-hidden="true">
        <rect class="tile" x="4" y="4" width="92" height="92" rx="18"/>
        <g class="glyph">
          <path d="M26,28 V74 M74,28 V74"/>
          <path d="M26,36 H74 M26,48 H74 M26,60 H74"/>
          <path d="M22,74 H78"/>
        </g>
      </svg>
      <p class="service__label">Fencing &amp; Decking</p>
    </div>
    <div class="service" style="left:708px;top:140px">
      <svg class="service__icon" viewBox="0 0 100 100" aria-hidden="true">
        <rect class="tile" x="4" y="4" width="92" height="92" rx="18"/>
        <g class="glyph">
          <path d="M24,70 H76"/>
          <path d="M30,70 L28,54 M38,70 L38,46 M46,70 L48,50 M54,70 L54,42 M62,70 L64,50 M70,70 L72,56"/>
        </g>
      </svg>
      <p class="service__label">Artificial Grass</p>
    </div>
  </section>

  <footer>
    <div class="contact">
      <span class="contact__cta">Call today for your FREE estimate!</span>
      <span class="contact__phone">
        <svg width="32" height="32" viewBox="0 0 32 32" aria-hidden="true">
          <circle cx="16" cy="16" r="14" fill="none" stroke="var(--ink)" stroke-width="2.5"/>
          <path d="M11,9 L14,9 L15,13 L13,14.5 C14,17 15,18 17.5,19 L19,17 L23,18 L23,21 C23,22 22,23 21,23 C15,22.5 9.5,17 9,11 C9,10 10,9 11,9 Z" fill="var(--ink)"/>
        </svg>
        07700 900 418
      </span>
    </div>
    <p class="contact__web">www.brackmoor-yards.com</p>
    <div class="social">
      <span class="social__square"></span>
      <span class="social__square"></span>
      <span class="social__square"></span>
    </div>
  </footer>
</main>
</body>
</html>
```